Financial Coaching & Personal Development

I’m desiring a classic business card for my financial coaching and personal development business. The colors I have started with are a goldish brown and hunter green. The brownish color represents soil and green represents growth. I don’t want it it to look masculine. I want the brown to be more of a golden color. I want the color combination and overall design to be timeless not trendy. The logo can be changed as long as it represents growth- moving from where you are to where you want to be.

Target Market(s)

Working Adults with median income $65k; small businesses with a minimum of 20 employees

Industry/Entity Type

Consulting

Contact Information for Business Card

Marla Pettit, MBA
Certified Financial Coach

Font styles to use
Serif

Requirements
Must have
• Logo
My name
Business description
Email marla.pettit@brightwaycoachhub
Phone number 555-314-7829
Nice to have
• Slogan

```html
<!DOCTYPE html>
<html lang="en">
<head>
<meta charset="utf-8">
<title>Brightway Coach Hub – Business Card</title>
<link href="https://fonts.googleapis.com/css2?family=Libre+Baskerville:wght@400;700&display=swap" rel="stylesheet">
<style>
  :root {
    --hunter-green: #239449;
    --golden-brown: #8c6a2b;
    --ink: #1f1f1f;
    --paper: #ffffff;
    --backdrop: #e9e6e1;
    --faint-green: #e6f1ea;
  }
  * { margin: 0; padding: 0; box-sizing: border-box; }
  html, body {
    width: 1200px; height: 960px; overflow: hidden;
    background: var(--backdrop);
    font-family: "Libre Baskerville", Georgia, serif;
  }
  .stage {
    width: 1200px; height: 960px;
    display: flex; flex-direction: column;
    align-items: center; justify-content: center; gap: 56px;
  }
  .card {
    position: relative;
    width: 640px; height: 366px;
    box-shadow: 0 10px 28px rgba(0,0,0,.18);
    overflow: hidden;
  }

  /* Front */
  .card-front {
    background: var(--hunter-green);
    color: var(--paper);
    display: flex; flex-direction: column; align-items: center; justify-content: center;
    text-align: center;
  }
  .brand-mark { display: flex; flex-direction: column; align-items: center; }
  .brand-square {
    width: 46px; height: 46px; border: 3px solid currentColor; margin-bottom: 18px;
  }
  .brand-name {
    font-weight: 700; font-size: 25px; letter-spacing: 2px; text-transform: uppercase;
  }
  .brand-tagline { font-size: 12px; margin-top: 5px; letter-spacing: .3px; }
  .slogan { font-size: 17px; margin-top: 46px; }

  /* Back */
  .card-back { background: var(--paper); color: var(--ink); }
  .back-brand {
    position: absolute; left: 48px; top: 52px;
    display: flex; flex-direction: column; align-items: flex-start;
  }
  .back-brand .brand-square {
    width: 40px; height: 40px; border-color: var(--hunter-green); margin-left: 44px; margin-bottom: 14px;
  }
  .back-brand .brand-name { color: var(--golden-brown); font-size: 18px; letter-spacing: 1.4px; }
  .back-brand .brand-tagline { color: var(--hunter-green); font-size: 9.5px; margin-top: 3px; }

  .faint-brand {
    position: absolute; right: 40px; top: 70px;
    width: 200px; height: 200px; border-radius: 50%;
    background: var(--faint-green);
  }

  .contact-block { position: absolute; left: 48px; bottom: 40px; }
  .person-name { font-size: 26px; color: var(--hunter-green); }
  .person-name .credential { color: var(--golden-brown); }
  .person-role { font-size: 15px; margin-top: 4px; }
  .contact-list { list-style: none; margin-top: 18px; }
  .contact-list li {
    display: flex; align-items: center; gap: 9px; font-size: 14.5px; margin-top: 5px;
  }
  .contact-list svg { width: 12px; height: 12px; fill: var(--hunter-green); flex: none; }
</style>
</head>
<body>
<main class="stage">

  <section class="card card-front">
    <div class="brand-mark">
      <span class="brand-square"></span>
      <span class="brand-name">Brightway Coach Hub</span>
      <span class="brand-tagline">Financial Education &amp; Personal Development</span>
    </div>
    <p class="slogan">Here Is your Slogan</p>
  </section>

  <section class="card card-back">
    <div class="faint-brand" aria-hidden="true"></div>

    <div class="back-brand">
      <span class="brand-square"></span>
      <span class="brand-name">Brightway Coach Hub</span>
      <span class="brand-tagline">Financial Education &amp; Personal Development</span>
    </div>

    <div class="contact-block">
      <h1 class="person-name">Marla Pettit<span class="credential">, MBA</span></h1>
      <p class="person-role">Certified Financial Coach</p>
      <ul class="contact-list">
        <li>
          <svg viewBox="0 0 24 24" aria-label="Phone"><path d="M6.6 10.8a15.2 15.2 0 0 0 6.6 6.6l2.2-2.2a1 1 0 0 1 1-.25 11.4 11.4 0 0 0 3.6.57 1 1 0 0 1 1 1V20a1 1 0 0 1-1 1A17 17 0 0 1 3 4a1 1 0 0 1 1-1h3.5a1 1 0 0 1 1 1c0 1.25.2 2.45.57 3.57a1 1 0 0 1-.25 1z"/></svg>
          <span>555-314-7829</span>
        </li>
        <li>
          <svg viewBox="0 0 24 24" aria-label="Email"><path d="M2 5h20v14H2z M4 7v.5l8 5 8-5V7l-8 5z" fill-rule="evenodd"/></svg>
          <span>marla.pettit@brightwaycoachhub</span>
        </li>
      </ul>
    </div>
  </section>

</main>
</body>
</html>
```